R.Wren Customer Retention Business Infographic

I am looking to create an infographic by transforming the following data to be used on my website and proposals. I have specific colors that I would like to blend with and a concept of what it could look like, but open. I want to be able to show the comparison...of the two data points side by side.

Target Market(s)

Passionate Business owners

Industry/Entity Type

Business consulting

Font styles to use
Sans Serif

Requirements
Must have
• Concise infographic side by side comparision to use on website and proposals

```html
<!DOCTYPE html>
<html lang="en">
<head>
<meta charset="utf-8">
<title>R.Wren Customer Retention Infographic</title>
<link rel="stylesheet" href="https://fonts.googleapis.com/css2?family=Open+Sans:wght@400;600;700;800&display=swap">
<style>
  :root {
    --backdrop: #646464;
    --navy: #1c2955;
    --slate-blue: #5f7da7;
    --card: #f2f2f2;
    --gain-yellow: #fdd46c;
    --cost-orange: #fbbe6a;
    --ring-grey: #c9c9c9;
    --icon-disc: #c2c8d9;
    --arc-blue: #5a77a6;
    --white: #ffffff;
  }
  * { box-sizing: border-box; margin: 0; padding: 0; }
  html, body { width: 1200px; height: 763px; overflow: hidden; }
  body {
    background: var(--backdrop);
    font-family: "Open Sans", Arial, sans-serif;
    position: relative;
  }
  .infographic {
    position: absolute;
    left: 128px; top: 93px;
    width: 966px; height: 593px;
    background: var(--card);
    box-shadow: 6px 8px 14px rgba(0,0,0,.35);
    overflow: hidden;
  }
  .title-band {
    position: absolute; left: 0; top: 0;
    width: 100%; height: 99px;
    background: var(--navy);
    display: flex; align-items: center; justify-content: center;
  }
  .title {
    color: var(--white);
    font-weight: 700;
    font-size: 27px;
    letter-spacing: .2px;
    text-transform: uppercase;
  }
  .footer-band {
    position: absolute; left: 0; bottom: 0;
    width: 100%; height: 13px;
    background: var(--navy);
  }
  .column-heads {
    position: absolute; left: 95px; top: 118px;
    width: 789px; height: 78px;
    background: var(--slate-blue);
    border-radius: 18px 18px 0 0;
    color: var(--white);
    font-size: 15px; line-height: 20px;
  }
  .column-head {
    position: absolute; top: 8px; width: 320px; text-align: center;
  }
  .column-head.gain { left: 20px; }
  .column-head.cost { right: 18px; }
  .fact {
    position: absolute;
    width: 337px; height: 77px;
    color: var(--white);
    font-size: 14px; line-height: 19px;
    display: flex; flex-direction: column; justify-content: center;
    padding: 0 18px;
  }
  .fact::after {
    content: ""; position: absolute; top: 12px;
    border-top: 7px solid transparent; border-bottom: 7px solid transparent;
  }
  .fact.gain {
    left: 95px; background: var(--gain-yellow); text-align: right;
    border-radius: 0 4px 4px 0;
  }
  .fact.gain::after { right: -7px; border-left: 7px solid var(--gain-yellow); }
  .fact.cost {
    left: 546px; background: var(--cost-orange); text-align: left;
    border-radius: 4px 0 0 4px;
  }
  .fact.cost::after { left: -7px; border-right: 7px solid var(--cost-orange); }
  .row-1 { top: 207px; }
  .row-2 { top: 296px; }
  .row-3 { top: 384px; }
  .row-4 { top: 473px; }
  .timeline {
    position: absolute; left: 452px; top: 210px;
    width: 76px; height: 380px;
  }
</style>
</head>
<body>
  <main class="infographic">
    <header class="title-band">
      <h1 class="title">When customers engage businesses flourish</h1>
    </header>

    <div class="column-heads">
      <p class="column-head gain">When your customers are happy and your business becomes an essential part of their lives… you experience</p>
      <p class="column-head cost">When your customers are not ecstatic, you are stuck with stagnant growth and dropping retention rate … it costs you</p>
    </div>

    <p class="fact gain row-1">Boost profits by 25% to 95% with 5% increase in customer retention</p>
    <p class="fact gain row-2">65% of your business comes from repeat customers.</p>
    <p class="fact gain row-3">60% of loyal customers will talk about YOU with their friends and family.</p>
    <p class="fact gain row-4">60-70% probability of selling to an existing customer</p>

    <p class="fact cost row-1">5x higher cost to acquire new customers than retain existing ones</p>
    <p class="fact cost row-2">Costs 16 times more to build a long-term relationship with a new customer.</p>
    <p class="fact cost row-3">5% to 20% probability of selling to a new prospect</p>
    <p class="fact cost row-4"></p>

    <svg class="timeline" viewBox="0 0 76 380" aria-hidden="true">
      <line x1="38" y1="40" x2="38" y2="360" stroke="var(--ring-grey)" stroke-width="2"/>
      <g fill="none" stroke-width="2">
        <!-- node 1: chart -->
        <g transform="translate(38,40)">
          <circle r="33" fill="var(--card)" stroke="var(--ring-grey)"/>
          <path d="M-30 12 A32 32 0 0 1 -12 -29" stroke="var(--arc-blue)" stroke-width="5"/>
          <path d="M12 29 A32 32 0 0 0 30 12" stroke="var(--arc-blue)" stroke-width="5"/>
          <circle r="27" fill="var(--icon-disc)" stroke="none"/>
          <g stroke="var(--white)" stroke-width="2.5">
            <line x1="-10" y1="12" x2="-10" y2="4"/>
            <line x1="-4" y1="12" x2="-4" y2="0"/>
            <line x1="2" y1="12" x2="2" y2="6"/>
            <circle cx="5" cy="-6" r="7"/>
            <line x1="-12" y1="-2" x2="-2" y2="-10"/>
          </g>
        </g>
        <!-- node 2: group -->
        <g transform="translate(38,129)">
          <circle r="33" fill="var(--card)" stroke="var(--ring-grey)"/>
          <path d="M-12 -30 A32 32 0 0 1 31 8" stroke="var(--arc-blue)" stroke-width="5"/>
          <circle r="27" fill="var(--icon-disc)" stroke="none"/>
          <g stroke="var(--white)" stroke-width="2.5">
            <circle cx="-7" cy="-4" r="5"/>
            <circle cx="7" cy="-4" r="5"/>
            <path d="M-16 12 q9 -12 18 0"/>
            <path d="M-2 12 q9 -12 18 0"/>
          </g>
        </g>
        <!-- node 3: speech -->
        <g transform="translate(38,218)">
          <circle r="33" fill="var(--card)" stroke="var(--ring-grey)"/>
          <path d="M-31 -8 A32 32 0 0 0 -8 31" stroke="var(--arc-blue)" stroke-width="5"/>
          <circle r="27" fill="var(--icon-disc)" stroke="none"/>
          <g stroke="var(--white)" stroke-width="2.5">
            <rect x="-6" y="-15" width="18" height="11" rx="2"/>
            <circle cx="-4" cy="3" r="5"/>
            <path d="M-12 16 q8 -10 16 0"/>
          </g>
        </g>
        <!-- node 4: search -->
        <g transform="translate(38,307)">
          <circle r="33" fill="var(--card)" stroke="var(--ring-grey)"/>
          <path d="M-24 -22 A32 32 0 0 1 31 -6" stroke="var(--arc-blue)" stroke-width="5"/>
          <circle r="27" fill="var(--icon-disc)" stroke="none"/>
          <g stroke="var(--white)" stroke-width="2.5">
            <circle cx="-3" cy="-3" r="9"/>
            <line x1="4" y1="4" x2="13" y2="13" stroke-width="4"/>
          </g>
          <text x="-3" y="1" fill="var(--white)" font-size="10" font-weight="700" text-anchor="middle" font-family="Open Sans, sans-serif">$</text>
        </g>
      </g>
    </svg>

    <div class="footer-band"></div>
  </main>
</body>
</html>
```